Personal Motivational Quote Poster Design

I would like to create a poster with some of my favorite quotes to hang in my office. I did similar projects in 2012 and 2014. I've uploaded the winning designs so you can get a better idea of what I'm looking for. I will provide feedback on your design within 24 hours of receiving it.

The poster must contain the following quotes:

“What the pupil must learn, if he learns anything at all, is that the world will do most of the work for you, provided you cooperate with it by identifying how it really works and aligning with those realities. If we do not let the world teach us, it teaches us a lesson.” - Walter Brindley

“I tackle every big new problem by asking two questions: Who has dealt with this problem well? And what can we learn from them?” - Hal Porter

“If we can really understand the problem, the answer will come out of it, because the answer is not separate from the problem.” - Ravel Ondashanti

“Success is nothing more than a few simple disciplines, practiced every day; while failure is simply a few errors in judgment, repeated every day. It is the accumulative weight of our disciplines and our judgments that leads us to either fortune or failure.” - Ned Calve

“Inaction breeds doubt and fear. Action breeds confidence and courage.” - Rex Halloway

“What’s the one thing you can do, such that by doing it, everything else will be easier or unnecessary?” - Lyle Danvers

Requirements
Must have
• The poster will be 24" high x 36" long and printed on canvas, so the image you create needs to have a resolution of at least 2700 x 3900.
Nice to have
• I don't have an exact vision for how the poster should look, so I am totally open to you using your creativity to develop, arrange and present the content as you'd like.

That said, I would like an image (photo or posterized image) of the person being quoted along with each quote. I do not have specific images that I would like you to use, so you will need to find the images on your own.

The images don't need to be perfect... I am more interested in the poster relating the essence of the quotes and the people being quoted than I am in perfect photographic images of the people being quoted.

```html
<!DOCTYPE html>
<html lang="en">
<head>
<meta charset="utf-8">
<title>Quote Poster</title>
<link rel="stylesheet" href="https://fonts.googleapis.com/css2?family=Raleway:ital,wght@1,500;1,700&display=swap">
<style>
  :root {
    --backdrop: #5b5b5b;
    --wall-light: #f6f6f4;
    --wall-shade: #e4e4e2;
    --sky: #12a7e6;
    --teal: #23a497;
    --ink: #0e0e0e;
    --text: #ffffff;
    --portrait-dark: #3d4a52;
    --portrait-light: #9aa6ad;
  }
  * { margin: 0; padding: 0; box-sizing: border-box; }
  html, body {
    width: 975px; height: 1200px; overflow: hidden;
    background: var(--backdrop);
  }
  .poster {
    position: absolute; left: 97px; top: 15px;
    width: 780px; height: 1170px; overflow: hidden;
  }
  .wall {
    position: absolute; inset: 0;
    background: linear-gradient(160deg, var(--wall-light), var(--wall-shade));
  }
  .shapes { position: absolute; inset: 0; }
  .shapes .fill-sky { fill: var(--sky); }
  .shapes .fill-teal { fill: var(--teal); }
  .shapes .outline { fill: none; stroke: var(--ink); stroke-width: 3; }
  .portrait {
    position: absolute; border-radius: 46% 46% 30% 30%;
    background: radial-gradient(ellipse at 50% 40%, var(--portrait-light), var(--portrait-dark) 75%);
  }
  .quote {
    position: absolute;
    font-family: "Raleway", sans-serif; font-style: italic; font-weight: 500;
    color: var(--text); font-size: 10.5px; line-height: 18px;
  }
  .quote cite {
    display: block; margin-top: 12px;
    font-style: italic; font-weight: 700; font-size: 11.5px;
  }
</style>
</head>
<body>
<main class="poster">
  <div class="wall" role="img" aria-label="White painted brick wall"></div>

  <svg class="shapes" width="780" height="1170" viewBox="0 0 780 1170" aria-hidden="true">
    <path class="fill-sky" d="M110,100 C190,70 330,95 420,110 C470,120 455,200 445,260 C435,320 330,330 230,322 C140,315 75,300 65,230 C55,160 60,118 110,100 Z"/>
    <path class="outline" d="M90,85 C160,40 300,40 400,55 C460,65 460,150 455,220 C450,300 360,315 250,318 C150,320 60,310 50,220 C42,150 40,110 90,85 Z"/>

    <path class="fill-teal" d="M520,150 C580,110 660,105 720,115 C765,125 760,200 745,250 C725,300 640,310 570,302 C500,295 455,280 458,230 C460,190 470,180 520,150 Z"/>
    <path class="outline" d="M470,170 C500,125 600,130 680,118 C760,108 765,190 740,240 C715,300 620,315 540,305 C470,297 440,220 470,170 Z"/>

    <path class="fill-teal" d="M220,380 C300,345 420,360 520,375 C600,390 610,470 590,540 C570,600 480,612 380,615 C290,618 200,610 178,540 C160,480 160,410 220,380 Z"/>
    <path class="outline" d="M200,370 C300,335 450,355 540,370 C600,385 600,470 570,540 C540,610 420,625 320,620 C220,615 150,600 145,520 C140,440 150,395 200,370 Z"/>

    <path class="fill-sky" d="M90,670 C180,645 320,650 390,665 C430,680 430,760 420,820 C410,890 330,912 230,912 C140,912 60,905 42,830 C30,760 30,690 90,670 Z"/>
    <path class="outline" d="M60,680 C110,630 300,630 380,660 C440,685 425,780 400,840 C375,900 260,905 170,900 C90,895 30,860 35,780 C38,730 40,700 60,680 Z"/>

    <path class="fill-sky" d="M510,645 C580,618 680,625 725,640 C755,660 750,740 735,780 C715,820 620,822 550,818 C490,815 458,790 460,730 C462,680 470,660 510,645 Z"/>
    <path class="outline" d="M490,640 C540,605 650,605 710,620 C760,635 755,730 730,780 C705,822 600,815 530,812 C470,808 450,770 455,710 C458,670 465,655 490,640 Z"/>

    <path class="fill-teal" d="M380,900 C470,868 600,875 670,895 C710,915 705,1010 695,1080 C680,1140 590,1148 480,1148 C390,1148 340,1130 330,1060 C320,990 320,920 380,900 Z"/>
    <path class="outline" d="M360,880 C430,840 560,845 650,860 C720,875 715,980 700,1060 C685,1140 560,1160 450,1155 C370,1150 320,1120 325,1040 C330,960 320,905 360,880 Z"/>
  </svg>

  <div class="portrait" role="img" aria-label="Portrait of Walter Brindley" style="left:73px;top:110px;width:148px;height:178px"></div>
  <blockquote class="quote" style="left:227px;top:102px;width:175px">
    “What the pupil must learn, if he learns anything at all, is that the world will do most of the work for you, provided you cooperate with it by identifying how it really works and aligning with those realities. If we do not let the world teach us, it teaches us a lesson.”
    <cite>Walter Brindley</cite>
  </blockquote>

  <div class="portrait" role="img" aria-label="Portrait of Rex Halloway" style="left:620px;top:132px;width:112px;height:146px"></div>
  <blockquote class="quote" style="left:497px;top:155px;width:120px">
    “Inaction breeds doubt and fear. Action breeds confidence and courage.”
    <cite>Rex Halloway</cite>
  </blockquote>

  <div class="portrait" role="img" aria-label="Portrait of Hal Porter" style="left:215px;top:385px;width:117px;height:200px"></div>
  <blockquote class="quote" style="left:357px;top:432px;width:188px">
    “I tackle every big new problem by asking two questions: Who has dealt with this problem well? And what can we learn from them?”
    <cite>Hal Porter</cite>
  </blockquote>

  <div class="portrait" role="img" aria-label="Portrait of Ravel Ondashanti" style="left:73px;top:700px;width:117px;height:194px"></div>
  <blockquote class="quote" style="left:218px;top:713px;width:185px">
    “If we can really understand the problem, the answer will come out of it, because the answer is not separate from the problem.”
    <cite>Ravel Ondashanti</cite>
  </blockquote>

  <div class="portrait" role="img" aria-label="Portrait of Lyle Danvers" style="left:623px;top:651px;width:86px;height:132px"></div>
  <blockquote class="quote" style="left:499px;top:670px;width:130px">
    “What’s the one thing you can do, such that by doing it, everything else will be easier or unnecessary?”
    <cite>Lyle Danvers</cite>
  </blockquote>

  <div class="portrait" role="img" aria-label="Portrait of Ned Calve" style="left:543px;top:917px;width:123px;height:150px"></div>
  <blockquote class="quote" style="left:370px;top:925px;width:180px">
    “Success is nothing more than a few simple disciplines, practiced every day; while failure is simply a few errors in judgment, repeated every day. It is the accumulative weight of our disciplines and our judgments that leads us to either fortune or failure.”
    <cite>Ned Calve</cite>
  </blockquote>
</main>
</body>
</html>
```